Brevora web site / landing page

Looking for design help with building a landing page for our company and possible the remaining site. We are an AI developer and customer software developer company. Uploading logos for color scheme attached in logo xip file.

Target Market(s)

Manufacturing, Small business, Sales

Coding

Coded - Design and coding required

Number of Pages Required

3 page

Colors

Designer to choose colors to be used in the design.

Requirements
Must have
• Landing page, additional pages for AI, Custom software and Customer Portals explanation.

```html
<!DOCTYPE html>
<html lang="en">
<head>
<meta charset="utf-8">
<title>Brevora – AI &amp; Software Development</title>
<link href="https://fonts.googleapis.com/css2?family=Montserrat:wght@400;500&family=Open+Sans:wght@400;600&display=swap" rel="stylesheet">
<style>
:root{
  --blue:#1e6fc0;
  --navy:#0b1f5c;
  --deep:#06103a;
  --band:#e3ebf7;
  --card-text:#f1f5fb;
  --ink:#333a45;
  --muted:#6a717c;
  --footer:#141414;
  --purple:#8a3fe0;
  --white:#ffffff;
}
*{margin:0;padding:0;box-sizing:border-box}
html,body{width:1200px;height:2760px;overflow:hidden}
body{position:relative;background:var(--white);font-family:'Open Sans',sans-serif;color:var(--ink)}
.abs{position:absolute}
.heading{font-family:'Montserrat',sans-serif;font-weight:400;color:var(--blue);text-align:center;width:1200px;left:0;font-size:33px}

/* header */
.header{top:0;left:0;width:1200px;height:105px;background:var(--white)}
.brand{left:145px;top:34px;display:flex;align-items:center;gap:10px;font-family:'Montserrat',sans-serif;font-size:22px;letter-spacing:5px;color:var(--navy)}
.brand-dot{width:22px;height:22px;border-radius:50%;background:var(--navy)}
.nav{top:44px;font-family:'Montserrat',sans-serif;font-size:13.5px;color:#555}
.nav a{position:absolute;white-space:nowrap;color:inherit;text-decoration:none}
.nav a.active{color:var(--blue)}
.login{left:967px;top:33px;width:88px;height:40px;background:var(--blue);color:var(--white);font-family:'Montserrat',sans-serif;font-size:12px;display:flex;align-items:center;justify-content:center;gap:6px}

/* hero */
.hero{top:105px;left:0;width:1200px;height:646px}
.hero-title{right:145px;top:375px;text-align:right;font-family:'Montserrat',sans-serif;font-weight:400;font-size:46px;line-height:48px;letter-spacing:-0.5px}
.hero-title .l1{color:var(--purple)}
.hero-title .l2{background:linear-gradient(90deg,#3a6dff,#6ad4ff);-webkit-background-clip:text;background-clip:text;color:transparent}
.hero-title .l3{color:var(--white);font-size:38px;margin-top:6px}

.intro{top:870px;left:145px;width:910px;text-align:center;font-size:14.5px;line-height:27.5px}

/* services */
.card{top:1183px;width:297px;height:176px;background:var(--white);box-shadow:0 2px 6px rgba(0,0,0,.08);text-align:center;font-family:'Montserrat',sans-serif;font-size:18px;line-height:24px;color:var(--navy)}
.card svg{display:block;margin:24px auto 14px}

/* blog */
.post-img{top:1677px;width:296px;height:191px}
.post-body{top:1853px;width:272px;height:192px;background:var(--card-text);padding:22px 16px 0}
.post-body h3{font-family:'Montserrat',sans-serif;font-weight:400;font-size:16.5px;line-height:22.5px;color:#222}
.post-body p{font-size:10.5px;line-height:16px;color:var(--muted);margin-top:12px}
.post-body a{display:block;margin-top:14px;font-family:'Montserrat',sans-serif;font-size:13.5px;color:var(--blue);text-decoration:none}

/* contact */
.field{height:40px;background:var(--white);border:1px solid #d6dde8;font-size:11.5px;color:#666;padding:0 15px;display:flex;align-items:center;justify-content:space-between}
.submit{left:556px;top:2457px;width:88px;height:40px;background:var(--blue);color:var(--white);font-family:'Montserrat',sans-serif;font-size:12px;display:flex;align-items:center;justify-content:center}

/* footer */
.foot-links{left:143px;top:2668px;font-size:11.5px;color:#8a8f96;word-spacing:2px}
.copyright{left:143px;top:2701px;font-size:11.5px;color:#8a8f96}
.social{top:2684px;width:16px;height:16px;border-radius:50%;background:#6c6f75}
</style>
</head>
<body>

<!-- header -->
<header class="abs header">
  <div class="abs brand"><span class="brand-dot"></span>BREVORA</div>
  <nav class="abs nav" style="left:0;width:1200px">
    <a class="active" style="left:564px">Home</a>
    <a style="left:636px">About Us</a>
    <a style="left:728px">Services</a>
    <a style="left:812px">Blog</a>
    <a style="left:875px">Contact Us</a>
  </nav>
  <div class="abs login">
    <svg width="11" height="11" viewBox="0 0 11 11"><circle cx="5.5" cy="3" r="2.6" fill="#fff"/><path d="M0.5 11c0-3 2.2-4.6 5-4.6s5 1.6 5 4.6z" fill="#fff"/></svg>LOG IN
  </div>
</header>

<!-- hero -->
<section class="abs hero">
  <svg width="1200" height="646" viewBox="0 0 1200 646" role="img" aria-label="Digital illustration of an artificial intelligence head formed from glowing network lines">
    <defs>
      <radialGradient id="heroGlow" cx="0.3" cy="0.45" r="0.7">
        <stop offset="0" stop-color="#1d7cf0"/>
        <stop offset="0.45" stop-color="#0d2a8a"/>
        <stop offset="1" stop-color="#050d33"/>
      </radialGradient>
    </defs>
    <polygon points="0,0 1200,0 1200,511 600,646 0,511" fill="url(#heroGlow)"/>
  </svg>
  <svg class="abs" style="left:52px;top:235px" width="24" height="36" viewBox="0 0 24 36"><polyline points="20,3 5,18 20,33" fill="none" stroke="#fff" stroke-width="4"/></svg>
  <svg class="abs" style="left:1122px;top:235px" width="24" height="36" viewBox="0 0 24 36"><polyline points="4,3 19,18 4,33" fill="none" stroke="#fff" stroke-width="4"/></svg>
  <div class="abs" style="left:1067px;top:260px;width:4px;height:132px;background:#2f7bff"></div>
  <h1 class="abs hero-title" style="top:272px">
    <div class="l1">ARTIFICIAL</div>
    <div class="l2">INTELLIGENCE</div>
    <div class="l3">WITH RESULTS</div>
  </h1>
</section>

<!-- welcome -->
<h2 class="abs heading" style="top:823px">Welcome to Brevora</h2>
<p class="abs intro">At Brevora, we provide critical AI and automation systems that have dramatically increased efficiencies and profitability for our customers. We have established long term relationships with many companies in the aerospace, medical and finance industries, among others. Let us help your company automate tasks so that you can focus on growing your business. Contact us today for an on-site visit to get started reaping the benefits of AI.</p>

<!-- services band -->
<svg class="abs" style="left:0;top:1055px" width="1200" height="486" viewBox="0 0 1200 486"><polygon points="0,0 1200,0 1200,350 600,486 0,350" fill="var(--band)"/></svg>
<h2 class="abs heading" style="top:1127px">Services</h2>

<div class="abs card" style="left:144px">
  <svg width="64" height="70" viewBox="0 0 64 70" fill="none" stroke="var(--navy)" stroke-width="2.4"><path d="M32 4C20 4 12 10 12 20c-6 4-8 12-4 20 0 12 10 24 24 24s24-12 24-24c4-8 2-16-4-20 0-10-8-16-20-16z"/><line x1="32" y1="6" x2="32" y2="64"/><circle cx="22" cy="26" r="3"/><circle cx="42" cy="40" r="3"/><path d="M22 29v12h10M42 37V24H32"/></svg>
  AI Developer
</div>
<div class="abs card" style="left:451px">
  <svg width="70" height="70" viewBox="0 0 70 70" fill="none" stroke="var(--navy)" stroke-width="2.4"><circle cx="16" cy="16" r="9"/><circle cx="16" cy="16" r="3"/><circle cx="54" cy="14" r="9"/><circle cx="54" cy="14" r="3"/><path d="M28 66V40c0-3 5-3 5 0V28c0-3 5-3 5 0v14l6 2c3 1 4 4 4 7v15"/><path d="M6 40h14M52 38h12M44 24l-8 6"/></svg>
  Customer Software<br>Developer
</div>
<div class="abs card" style="left:759px">
  <svg width="60" height="70" viewBox="0 0 60 70" fill="none" stroke="var(--navy)" stroke-width="2.4"><circle cx="30" cy="6" r="3"/><circle cx="14" cy="12" r="3"/><circle cx="46" cy="12" r="3"/><circle cx="6" cy="26" r="3"/><circle cx="54" cy="26" r="3"/><circle cx="10" cy="40" r="3"/><circle cx="50" cy="40" r="3"/><path d="M30 9v30M16 14l10 20M44 14l-10 20M9 27l17 10M51 27l-17 10M13 40h12M47 40H35"/><path d="M24 66V44c0-3 5-3 5 0v-4c0-3 5-3 5 0v6l5 2c2 1 3 3 3 5v13"/></svg>
  Customer Portals
</div>

<!-- blog -->
<h2 class="abs heading" style="top:1615px">Blog</h2>
<svg class="abs" style="left:54px;top:1758px" width="20" height="32" viewBox="0 0 20 32"><polyline points="17,3 4,16 17,29" fill="none" stroke="#666" stroke-width="3"/></svg>
<svg class="abs" style="left:1126px;top:1758px" width="20" height="32" viewBox="0 0 20 32"><polyline points="3,3 16,16 3,29" fill="none" stroke="#666" stroke-width="3"/></svg>

<div class="abs post-img" role="img" aria-label="Glowing digital brain on a dark blue background" style="left:144px;background:radial-gradient(circle at 50% 55%,#c02a6a 0,#3a2a9a 30%,#0a1a55 70%)"></div>
<div class="abs post-img" role="img" aria-label="Person wearing a virtual reality headset in a bright tunnel" style="left:452px;background:radial-gradient(circle at 50% 40%,#ffe2b8 0,#c86a4a 25%,#1c2e5a 65%,#0c1430 100%)"></div>
<div class="abs post-img" role="img" aria-label="Business team with network lines overlaid" style="left:759px;background:linear-gradient(160deg,#c9d7f0 0,#5a78b4 45%,#142a66 100%)"></div>

<article class="abs post-body" style="left:156px">
  <h3>Fusce vitae lectus amet mi pulvinar maximus. Aenean placerat nibh accumsan</h3>
  <p>Nunc sit amet consequat risus. Curabitur ac elit leo. In eleifend dui tellus, in scelerisque elit porttitor et. Integer eu massa lacinia.</p>
  <a>READ MORE</a>
</article>
<article class="abs post-body" style="left:464px">
  <h3>Sed libero felis, vestibulum et dolor eget, lacinia aliquet neque&nbsp; molestie.</h3>
  <p>Nunc sit amet consequat risus. Curabitur ac elit leo. In eleifend dui tellus, in scelerisque elit porttitor et. Integer eu massa lacinia.</p>
  <a>READ MORE</a>
</article>
<article class="abs post-body" style="left:771px">
  <h3>Donec sit amet lectus nec mi tempor laoreet ac nec nunc auctor.</h3>
  <p>Nunc sit amet consequat risus. Curabitur ac elit leo. In eleifend dui tellus, in scelerisque elit porttitor et. Integer eu massa lacinia.</p>
  <a>READ MORE</a>
</article>

<!-- contact + footer -->
<div class="abs" style="left:0;top:2125px;width:1200px;height:635px;background:var(--band)"></div>
<svg class="abs" style="left:0;top:2505px" width="1200" height="255" viewBox="0 0 1200 255"><polygon points="0,0 600,135 1200,0 1200,255 0,255" fill="var(--footer)"/></svg>

<h2 class="abs heading" style="top:2198px">Contact us</h2>
<div class="abs field" style="left:144px;top:2250px;width:217px">Name</div>
<div class="abs field" style="left:375px;top:2250px;width:217px">Email</div>
<div class="abs field" style="left:606px;top:2250px;width:218px">Phone</div>
<div class="abs field" style="left:837px;top:2250px;width:218px">Service for
  <svg width="10" height="6" viewBox="0 0 10 6"><polyline points="1,1 5,5 9,1" fill="none" stroke="#555" stroke-width="1.3"/></svg>
</div>
<div class="abs field" style="left:144px;top:2307px;width:911px;height:128px;align-items:flex-start;padding-top:14px">Messages</div>
<div class="abs submit">SUBMIT</div>

<footer>
  <div class="abs foot-links">Home &nbsp;| &nbsp;About Us &nbsp;| &nbsp;Services &nbsp;| &nbsp;Blog &nbsp;| &nbsp;Contact Us</div>
  <div class="abs copyright">Copyright © 2019 &nbsp;Brevora. &nbsp; All rights reserved.</div>
  <span class="abs social" style="left:1001px"></span>
  <span class="abs social" style="left:1036px"></span>
</footer>

</body>
</html>
```